Publisher seeks book cover / Book cover for publishing house

Full cover (front, back and side of the book). 28 cm x 20 cm total (High 20 cm, width 13, side 2 cm) Front cover: Title of the author on top, centered (Aurélien Castaigne) Title: Charting the skies Subtitle: Working pilot aerial Bottom and centered: attached logo (Velmora Editions) in white, and edited eventualy. Side: From left to right: Editor logo (only "Velmora" word, without the "Editions" word, title and author name Back cover: Left text column ) Bottom: space available for the bar coded price and 2 or 3 lines of text Right text column (approx 6.5 cm wide) Bottom of the right colum, center of the right column: same attached logo (Velmora Editions) in white, and edited eventualy, with www.velmora-example.com below the logo. Left Lateral margin of the back cover, this book should be almost 1 cm)
Colors
Designer to choose colors to be used in the design.
Look and feel
Each slider illustrates characteristics of the customer's brand and the style your logo design should communicate.

```html
<!DOCTYPE html>
<html lang="en">
<head>
<meta charset="utf-8">
<title>Charting the Skies – Full Cover</title>
<link rel="stylesheet" href="https://fonts.googleapis.com/css2?family=Marcellus&family=Forum&family=Montserrat:wght@400&family=Cabin:wght@400&family=PT+Sans:wght@400;700&family=Arimo&display=swap">
<style>
  :root {
    --page-bg: #f6f5f7;
    --paper: #ffffff;
    --author-brown: #4a2e12;
    --title-red: #b2161a;
    --subtitle-slate: #3b4856;
    --ink: #1d1d1d;
    --panel-navy-top: #4a6384;
    --panel-navy-bottom: #34435e;
    --panel-text: #f4f6fa;
    --brand-green: #3d6b1a;
    --spine-teal: #9fd6d6;
    --sky-light: #dbe3ec;
    --sea-dark: #4a5c72;
    --lagoon: #3ebccb;
    --lagoon-pale: #a9e3e2;
  }
  * { box-sizing: border-box; margin: 0; padding: 0; }
  html, body { width: 1200px; height: 806px; overflow: hidden; background: var(--page-bg); }
  .cover-spread {
    position: absolute; left: 67px; top: 35px; width: 1068px; height: 769px;
    background: linear-gradient(180deg, var(--paper) 0%, var(--paper) 20%, var(--sky-light) 55%, var(--paper) 100%);
    overflow: hidden;
    font-family: "Cabin", sans-serif;
  }
  .scenery {
    position: absolute; left: 0; right: 0; top: 430px; bottom: 0;
    background: linear-gradient(180deg,
      rgba(219,227,236,0) 0%,
      #cfd7e1 14%,
      #9aa9ba 28%,
      var(--sea-dark) 40%,
      #5aa7b8 48%,
      var(--lagoon) 56%,
      #6fd0d6 68%,
      var(--lagoon-pale) 84%,
      #f2f8f7 100%);
  }
  .spine-band {
    position: absolute; left: 497px; width: 77px; top: 0; bottom: 0;
    background: linear-gradient(180deg, var(--paper) 0%, #f1f8f8 40%, var(--spine-teal) 75%, #86cccc 100%);
  }

  /* Back cover */
  .back-column-left {
    position: absolute; left: 20px; top: 12px; width: 169px; height: 570px;
    background: linear-gradient(180deg, var(--panel-navy-top), var(--panel-navy-bottom));
    color: var(--panel-text);
    font-size: 14.4px; line-height: 18.4px;
    padding: 11px 2px 0 13px;
  }
  .back-column-left p + p { margin-top: 18.4px; }
  .back-note {
    position: absolute; left: 30px; top: 584px; width: 134px;
    text-align: center; font-family: "Arimo", sans-serif;
    font-size: 14.4px; line-height: 18.4px; color: var(--ink);
  }
  .barcode-space {
    position: absolute; left: 33px; top: 676px; width: 140px; height: 71px;
    background: var(--paper);
  }
  .back-column-right {
    position: absolute; left: 213px; top: 17px; width: 276px; height: 592px;
    background: rgba(255,255,255,0.92);
    border: 1px solid #222;
    color: var(--ink);
    font-size: 14.4px; line-height: 18.4px;
    padding: 4px 12px 0 10px;
  }
  .back-column-right p + p { margin-top: 18.4px; }

  .imprint {
    position: absolute; top: 682px; width: 111px; height: 57px;
    background: var(--paper);
    display: flex; flex-direction: column; align-items: center; justify-content: center;
    font-family: "PT Sans", sans-serif;
    color: var(--brand-green); font-weight: 700; line-height: 1;
  }
  .imprint-name { font-size: 23px; text-transform: uppercase; }
  .imprint-label { font-size: 15px; }
  .imprint--back { left: 290px; }
  .imprint--front { left: 759px; }

  /* Spine */
  .spine-imprint {
    position: absolute; left: 500px; top: 36px; width: 72px; text-align: center;
    font-family: "PT Sans", sans-serif;
    color: var(--brand-green); font-weight: 700; font-size: 17px; text-transform: uppercase;
  }
  .spine-text {
    position: absolute; writing-mode: vertical-rl; white-space: nowrap;
    font-family: "Marcellus", serif;
  }
  .spine-title-main { left: 515px; top: 78px; font-family: "Forum", serif; font-size: 38px; color: var(--title-red); letter-spacing: 1px; }
  .spine-title-sub { left: 521px; top: 275px; font-size: 29px; color: var(--subtitle-slate); letter-spacing: 4px; font-variant: small-caps; }
  .spine-author { left: 522px; top: 515px; font-size: 23px; color: var(--subtitle-slate); }

  /* Front cover */
  .front-cover {
    position: absolute; left: 574px; top: 0; width: 494px; text-align: center;
  }
  .front-author {
    margin-top: 38px; font-family: "Marcellus", serif; font-size: 48px; line-height: 1;
    font-weight: 400; color: var(--author-brown); letter-spacing: 1px;
  }
  .front-title {
    margin-top: 34px; font-family: "Forum", serif; font-size: 92px; line-height: 1;
    font-weight: 400; color: var(--title-red);
    text-shadow: 1px 1px 0 #6e0a0c;
  }
  .front-subtitle {
    margin-top: 46px; font-family: "Marcellus", serif; font-size: 60px; line-height: 1;
    color: var(--subtitle-slate); font-variant: small-caps; letter-spacing: 5px;
  }
  .front-tagline {
    margin-top: 18px; font-family: "Montserrat", sans-serif; font-size: 22px; color: #333;
  }
</style>
</head>
<body>
  <div class="cover-spread">
    <div class="scenery" role="img" aria-label="Photograph of a small seaplane flying over a turquoise lagoon with a mountainous island on the horizon"></div>
    <div class="spine-band"></div>

    <section class="back-cover">
      <div class="back-column-left">
        <p>Lorem ipsum dolor sit amet, consectetur adipiscing elit, sed do eiusmod tempor incididunt ut labore et dolore magna aliqua. Quis ipsum suspendisse ultrices gravida. Risus commodo viverra maecenas accumsan lacus vel facilisis.</p>
        <p>Lorem ipsum dolor sit amet, consectetur adipiscing elit, sed do eiusmod tempor incididunt ut labore et dolore magna aliqua. Quis ipsum suspendisse ultrices gravida. Risus commodo viverra maecenas accumsan lacus vel facilisis. amet, consectetur adipiscing elit, sed do e ultrices gravida. Risus commodo viverra maecenas accumsan lacus vel facilisis.</p>
      </div>
      <p class="back-note">Lorem ipsum dolor sit amet, consectetur adipiscing elit, sed</p>
      <div class="barcode-space"></div>

      <div class="back-column-right">
        <p>Lorem ipsum dolor sit amet, consectetur adipiscing elit, sed do eiusmod tempor incididunt ut labore et dolore magna aliqua. Quis ipsum suspendisse ultrices gravida. Risus commodo viverra maecenas accumsan lacus vel facilisis.</p>
        <p>Lorem ipsum dolor sit amet, consectetur adipiscing elit, sed do eiusmod tempor incididunt ut labore et dolore magna aliqua. Quis ipsum suspendisse ultrices gravida. Risus commodo viverra maecenas accumsan lacus vel facilisis.</p>
        <p>Lorem ipsum dolor sit amet, consectetur adipiscing elit, sed do eiusmod tempor incididunt ut labore et dolore magna aliqua. Quis ipsum suspendisse ultrices gravida. Risus commodo viverra maecenas accumsan lacus vel facilisis.</p>
        <p>Lorem ipsum dolor sit amet, consectetur adipiscing elit, sed do eiusmod tempor incididunt ut labore et dolore magna aliqua. Quis ipsum suspendisse ultrices gravida. Risus commodo viverra maecenas accumsan</p>
      </div>
      <div class="imprint imprint--back">
        <span class="imprint-label">Editions</span>
        <span class="imprint-name">Velmora</span>
      </div>
    </section>

    <section class="spine">
      <div class="spine-imprint">Velmora</div>
      <span class="spine-text spine-title-main">CHARTING</span>
      <span class="spine-text spine-title-sub">The Skies</span>
      <span class="spine-text spine-author">Aurélien Castaigne</span>
    </section>

    <section class="front-cover">
      <h2 class="front-author">Aurélien Castaigne</h2>
      <h1 class="front-title">CHARTING</h1>
      <p class="front-subtitle">The Skies</p>
      <p class="front-tagline">Working Pilot</p>
    </section>
    <div class="imprint imprint--front">
      <span class="imprint-label">Editions</span>
      <span class="imprint-name">Velmora</span>
    </div>
  </div>
</body>
</html>
```